Automotive eCommerce Business looking for a business card design

Looking for a clean and simple business card design. Our company name is "Tundra Motors" and we are a company specializing in the ecommerce sales of automotive parts, specifically for pick up trucks and large SUVs. Our company colours are red, black, and white.

Feel free to use the logo provided or create a new logo that you seem fit. Looking forward to your creative ideas!

Industry/Entity Type

Automotive

Contact Information for Business Card

We were thinking of a possibly two-sided design featuring just the logo and company name on one side, and personal information on the other side. Single sided designs will be considered as well.

Font styles to use
Serif
Sans Serif
Decorative

Colors
ec1f27
ffffff
000000

Requirements
Must have
• Space for employee's name, title, phone number and email address, along with the company address and website somewhere.

```html
<!DOCTYPE html>
<html lang="en">
<head>
<meta charset="utf-8">
<title>Tundra Motors Ltd. — Business Card</title>
<link rel="stylesheet" href="https://fonts.googleapis.com/css2?family=Montserrat:wght@400;500;700&display=swap">
<style>
  :root {
    --stage: #2c2c2c;
    --card: #f7f7f7;
    --card-shade: #e4e4e4;
    --ink: #1f1f1f;
    --ink-soft: #3d3d3d;
    --brand-red: #a61c22;
    --accent-tint: #d9c4bc;
    --accent-tint-deep: #c2aaa2;
  }
  * { margin: 0; padding: 0; box-sizing: border-box; }
  html, body { width: 1200px; height: 834px; overflow: hidden; }
  body {
    background: var(--stage);
    font-family: "Montserrat", Arial, sans-serif;
    display: flex;
    align-items: center;
    justify-content: center;
    gap: 36px;
  }
  .card {
    position: relative;
    width: 560px;
    height: 320px;
    background: linear-gradient(135deg, #ffffff 0%, var(--card) 55%, var(--card-shade) 100%);
    overflow: hidden;
    box-shadow: 0 14px 30px rgba(0,0,0,0.45);
  }

  /* Brand name block */
  .brand {
    display: flex;
    align-items: center;
    gap: 10px;
  }
  .brand-mark {
    width: 22px;
    height: 22px;
    background: var(--brand-red);
  }
  .brand-name {
    font-weight: 700;
    color: var(--ink);
    letter-spacing: 0.08em;
    text-transform: uppercase;
  }

  /* Front */
  .card-front {
    display: flex;
    flex-direction: column;
    align-items: center;
    justify-content: center;
  }
  .card-front .brand-mark { width: 30px; height: 30px; }
  .card-front .brand-name { font-size: 22px; }
  .front-web {
    margin-top: 10px;
    font-size: 12px;
    color: var(--brand-red);
    letter-spacing: 0.03em;
  }

  /* Back */
  .back-accent {
    position: absolute;
    right: -90px;
    top: -70px;
    width: 330px;
    height: 330px;
    border-radius: 50%;
    background: linear-gradient(160deg, var(--accent-tint) 0%, var(--accent-tint-deep) 100%);
    opacity: 0.75;
  }
  .back-content {
    position: absolute;
    left: 46px;
    top: 34px;
  }
  .card-back .brand-name { font-size: 15px; }
  .person-name {
    margin-top: 28px;
    font-size: 17px;
    font-weight: 700;
    color: var(--ink-soft);
  }
  .person-title {
    font-size: 12px;
    color: var(--brand-red);
    margin-top: 2px;
  }
  .company-line {
    margin-top: 12px;
    font-size: 11px;
    font-weight: 700;
    color: var(--brand-red);
    letter-spacing: 0.04em;
    text-transform: uppercase;
  }
  .address {
    font-size: 10px;
    color: var(--ink-soft);
    line-height: 1.6;
    margin-top: 3px;
    font-style: normal;
  }
  .contacts {
    list-style: none;
    margin-top: 12px;
  }
  .contacts li {
    display: flex;
    align-items: center;
    gap: 10px;
    font-size: 10.5px;
    color: var(--ink-soft);
    line-height: 1.9;
  }
  .contacts svg { width: 12px; height: 12px; fill: none; stroke: var(--brand-red); stroke-width: 1.6; }
</style>
</head>
<body>

  <section class="card card-front" aria-label="Card front">
    <div class="brand">
      <span class="brand-mark"></span>
      <span class="brand-name">Tundra Motors Ltd.</span>
    </div>
    <p class="front-web">www.tundramotors.example</p>
  </section>

  <section class="card card-back" aria-label="Card back">
    <div class="back-accent"></div>
    <div class="back-content">
      <div class="brand">
        <span class="brand-mark"></span>
        <span class="brand-name">Tundra Motors Ltd.</span>
      </div>
      <p class="person-name">Dale Hartley</p>
      <p class="person-title">President</p>
      <p class="company-line">Tundra Motors Ltd.</p>
      <address class="address">48 Ridgeline Road<br>2nd Floor Eastfield</address>
      <ul class="contacts">
        <li>
          <svg viewBox="0 0 12 12" aria-hidden="true"><path d="M2.5 1.5 L4.5 1.5 L5.2 3.8 L4 4.8 Q5 7 7.2 8 L8.2 6.8 L10.5 7.5 L10.5 9.5 Q10.5 10.5 9.5 10.5 Q2 10 1.5 2.5 Q1.5 1.5 2.5 1.5 Z"/></svg>
          203-555-0147
        </li>
        <li>
          <svg viewBox="0 0 12 12" aria-hidden="true"><rect x="1" y="2.5" width="10" height="7"/><path d="M1 2.5 L6 6.5 L11 2.5"/></svg>
          dale@tundramotors.example
        </li>
        <li>
          <svg viewBox="0 0 12 12" aria-hidden="true"><circle cx="6" cy="6" r="4.8"/><path d="M1.2 6 H10.8 M6 1.2 Q3.5 6 6 10.8 M6 1.2 Q8.5 6 6 10.8"/></svg>
          www.tundramotors.example
        </li>
      </ul>
    </div>
  </section>

</body>
</html>
```